Quill Refrigeration. Refrigeration and air conditioning specialists.

We need a website to promote our business. We would a modern simple design using the colours from our logo and black. We want it to be fun but proffesional.

Target Market(s)

Commercial

Number of Pages Required

4 page

Requirements
Must have
• Home Page, About Us, Services and Contact Us.
• 24/7 365 days service available.
• Quill Refrigeration's dedicated team specialises in commercial refrigeration and air conditioning equipment.
• Based in Joondalup, we cover Perth Metro and surrounding areas.
Nice to have
• KNOWLEDGE . EXPERIENCE . PASSION in bold.
• Our experienced and highly trained technicians provide extensive knowledge and exceptional skills for your commercial refrigeration and air conditioning requirements.
• Pictures of commercial refrigeration.
Should not have
• No mention of domestic services.

```html
<!DOCTYPE html>
<html lang="en">
<head>
<meta charset="utf-8">
<title>Quill Refrigeration</title>
<link rel="stylesheet" href="https://fonts.googleapis.com/css2?family=Lato:wght@400;700;900&display=swap">
<style>
:root{
  --lime:#9af25a;
  --purple:#2d1a4e;
  --ink:#1c1c1c;
  --text:#4a4a4a;
  --grey:#efefef;
  --white:#ffffff;
  --line:#d8d8d8;
}
*{box-sizing:border-box;margin:0;padding:0}
html,body{width:1200px;height:3327px;overflow:hidden}
body{position:relative;background:var(--white);font-family:'Lato',sans-serif;color:var(--text)}
.abs{position:absolute}
.brand{font-family:'Lato',sans-serif;font-weight:900;color:var(--lime);line-height:1}
.brand .name{font-size:44px;letter-spacing:1px;display:block}
.brand .sub{font-size:12px;letter-spacing:1px;display:block;margin-top:4px;padding-left:20px}
.nav{top:40px;left:488px;display:flex;gap:8px;font-size:15px;font-weight:700;color:var(--ink)}
.nav a{padding:8px 18px;text-decoration:none;color:var(--ink)}
.nav a.active{background:var(--lime)}
.header-phone{top:42px;left:930px;font-size:22px;font-weight:900;color:var(--purple);display:flex;align-items:center;gap:10px}
.hero{top:118px;left:0;width:1200px;height:560px;background:linear-gradient(120deg,#6e5a4c 0%,#8a7a6e 40%,#5d5d60 75%,#3f4145 100%)}
.hero-title{top:372px;left:0;width:1200px;text-align:center;font-size:43px;font-weight:900;color:var(--white);letter-spacing:1px}
.dots{top:634px;left:562px;display:flex;gap:10px}
.dots span{width:10px;height:10px;border-radius:50%;background:var(--white)}
.dots span.on{background:var(--lime)}
h2.section-title{font-size:28px;font-weight:900;color:var(--purple);text-align:center;letter-spacing:.5px}
.intro-text{top:788px;left:60px;width:1080px;text-align:center;font-size:15px;line-height:29px}
.btn{display:inline-block;background:var(--lime);color:var(--ink);font-weight:900;font-size:15px;text-align:center;line-height:42px;height:42px}
.band-grey{top:1022px;left:0;width:1200px;height:960px}
.photo{background:linear-gradient(135deg,#cfd2d4,#8d9297 60%,#5e6368)}
.feature-title{font-size:29px;font-weight:900;color:var(--purple)}
.feature-text{font-size:15px;line-height:24px;width:490px}
.offer-icon{width:104px;height:104px;border-radius:50%;background:var(--lime);display:flex;align-items:center;justify-content:center}
.offer-title{font-size:19px;font-weight:900;color:var(--ink);text-align:center;line-height:25px;width:340px}
.offer-text{font-size:15px;line-height:23px;text-align:center;width:300px}
.contact-band{top:2456px;left:0;width:1200px;height:646px}
.field{background:var(--white);border-radius:3px;font-size:15px;color:#555;padding:0 16px;line-height:50px;height:50px}
.footer-head{font-size:14px;font-weight:900;color:var(--purple);letter-spacing:.5px}
.footer-list{font-size:14px;line-height:33px;color:var(--ink);list-style:none}
.footer-contact{font-size:14px;color:var(--ink);line-height:21px}
.social{display:flex;gap:18px}
.social span{width:22px;height:22px;border-radius:50%;background:var(--ink);display:block}
</style>
</head>
<body>

<header>
  <div class="abs brand" style="top:22px;left:76px">
    <span class="name">QUILL</span>
    <span class="sub">REFRIGERATION</span>
  </div>
  <nav class="abs nav">
    <a class="active">HOME</a><a>ABOUT</a><a>SERVICES</a><a>CONTACT</a>
  </nav>
  <div class="abs header-phone">
    <svg width="18" height="18" viewBox="0 0 24 24"><path fill="#2d1a4e" d="M6.6 10.8a15 15 0 0 0 6.6 6.6l2.2-2.2a1 1 0 0 1 1-.25 11.4 11.4 0 0 0 3.6.6 1 1 0 0 1 1 1V20a1 1 0 0 1-1 1A17 17 0 0 1 3 4a1 1 0 0 1 1-1h3.5a1 1 0 0 1 1 1c0 1.25.2 2.45.6 3.6a1 1 0 0 1-.25 1z"/></svg>
    1-800-555-0147
  </div>
</header>

<section>
  <div class="abs hero" role="img" aria-label="Technician servicing a rooftop refrigeration unit"></div>
  <h1 class="abs hero-title">KNOWLEDGE . EXPERIENCE . PASSION</h1>
  <div class="abs dots"><span class="on"></span><span></span><span></span><span></span></div>
</section>

<section>
  <h2 class="abs section-title" style="top:730px;left:0;width:1200px">WELCOME TO OUR WEBSITE</h2>
  <p class="abs intro-text">Lorem ipsum dolor sit amet, consectetur adipiscing elit. In ut leo sit amet mauris<br>pellentesque lobortis. Praesent vulputate dictum venenatis. Pellentesque habitant morbi tristique senectus et netus et malesuada fames ac turpis egestas.<br>Quisque sodales, dolor non convallis condimentum, arcu diam feugiat ligula, eu tempus leo nibh ac mauris.<br>Cras a magna sit amet ex sagittis faucibus sit amet eget mauris.</p>
  <a class="abs btn" style="top:955px;left:524px;width:152px">READ MORE</a>
</section>

<section>
  <svg class="abs band-grey" viewBox="0 0 1200 960" preserveAspectRatio="none"><polygon points="0,68 1200,0 1200,898 0,960" fill="#efefef"/></svg>
  <div class="abs photo" style="top:1151px;left:75px;width:522px;height:351px" role="img" aria-label="Row of stainless steel commercial refrigerators"></div>
  <h3 class="abs feature-title" style="top:1188px;left:620px">COMMERCIAL REFRIGERATION</h3>
  <p class="abs feature-text" style="top:1243px;left:620px">Lorem ipsum dolor sit amet, consectetur adipiscing elit. In ut leo sit amet mauris pellentesque lobortis. Praesent vulputate dictum venenatis. Pellentesque habitant morbi tristique senectus et netus et malesuada fames ac turpis egestas. Quisque sodales, dolor non convallis condimentum, arcu diam feugiat ligula...</p>
  <a class="abs btn" style="top:1398px;left:620px;width:152px">READ MORE</a>

  <h3 class="abs feature-title" style="top:1548px;left:75px">AIR CONDITIONING EQUIPMENT</h3>
  <p class="abs feature-text" style="top:1603px;left:75px">Lorem ipsum dolor sit amet, consectetur adipiscing elit. In ut leo sit amet mauris pellentesque lobortis. Praesent vulputate dictum venenatis. Pellentesque habitant morbi tristique senectus et netus et malesuada fames ac turpis egestas. Quisque sodales, dolor non convallis condimentum, arcu diam feugiat ligula...</p>
  <a class="abs btn" style="top:1760px;left:75px;width:152px">READ MORE</a>
  <div class="abs photo" style="top:1502px;left:602px;width:523px;height:349px;background:linear-gradient(160deg,#6f7a78,#a9b0b1 50%,#585e60)" role="img" aria-label="Rooftop air conditioning condenser units"></div>
</section>

<section>
  <h2 class="abs section-title" style="top:2040px;left:0;width:1200px">WHAT WE OFFER</h2>

  <div class="abs offer-icon" style="top:2126px;left:188px">
    <svg width="46" height="46" viewBox="0 0 24 24"><circle cx="12" cy="12" r="10" fill="none" stroke="#1c1c1c" stroke-width="2.4"/><path d="M12 6.5V12l3.5 2.5" fill="none" stroke="#1c1c1c" stroke-width="2.4" stroke-linecap="round"/></svg>
  </div>
  <div class="abs offer-title" style="top:2250px;left:70px">24/7 365 DAYS SERVICE<br>AVAILABLE</div>
  <p class="abs offer-text" style="top:2304px;left:90px">Lorem ipsum dolor sit amet, consectetur adipiscing elit. In ut leo sit amet mauris pellentesque lobortis</p>

  <div class="abs offer-icon" style="top:2126px;left:548px">
    <svg width="48" height="48" viewBox="0 0 24 24"><path d="M6 9a6 6 0 0 1 12 0z" fill="#1c1c1c"/><rect x="5" y="9" width="14" height="1.6" fill="#1c1c1c"/><circle cx="12" cy="13" r="3" fill="#1c1c1c"/><path d="M4 22c0-4 3.6-6 8-6s8 2 8 6z" fill="#1c1c1c"/></svg>
  </div>
  <div class="abs offer-title" style="top:2250px;left:430px">EXPERIENCED &amp; HIGHLY TRAINED<br>TECHNICIANS</div>
  <p class="abs offer-text" style="top:2304px;left:450px">Lorem ipsum dolor sit amet, consectetur adipiscing elit. In ut leo sit amet mauris pellentesque lobortis</p>

  <div class="abs offer-icon" style="top:2126px;left:908px">
    <svg width="40" height="40" viewBox="0 0 24 24"><path d="M12 2a7 7 0 0 0-7 7c0 5 7 13 7 13s7-8 7-13a7 7 0 0 0-7-7zm0 9.5A2.5 2.5 0 1 1 12 6.5a2.5 2.5 0 0 1 0 5z" fill="#1c1c1c"/></svg>
  </div>
  <div class="abs offer-title" style="top:2250px;left:790px">SERVICE BASED IN<br>JOONDALUP</div>
  <p class="abs offer-text" style="top:2304px;left:810px">Lorem ipsum dolor sit amet, consectetur adipiscing elit. In ut leo sit amet mauris pellentesque lobortis</p>
</section>

<section>
  <svg class="abs contact-band" viewBox="0 0 1200 646" preserveAspectRatio="none" role="img" aria-label="Supermarket aisle with refrigerated display cases">
    <defs><linearGradient id="bandShade" x1="0" y1="0" x2="1" y2="1"><stop offset="0" stop-color="#4f5457"/><stop offset=".5" stop-color="#6b7073"/><stop offset="1" stop-color="#3e4245"/></linearGradient></defs>
    <polygon points="0,68 1200,0 1200,594 0,646" fill="url(#bandShade)"/>
  </svg>
  <h2 class="abs section-title" style="top:2570px;left:0;width:1200px;color:var(--white)">QUICK CONTACT</h2>
  <div class="abs field" style="top:2645px;left:227px;width:360px">Name</div>
  <div class="abs field" style="top:2645px;left:614px;width:359px">Phone Name</div>
  <div class="abs field" style="top:2712px;left:227px;width:360px">Email Address</div>
  <div class="abs field" style="top:2712px;left:614px;width:359px">Company Name</div>
  <div class="abs field" style="top:2778px;left:227px;width:746px;height:132px">Message</div>
  <a class="abs btn" style="top:2950px;left:524px;width:152px">SUBMIT</a>
</section>

<footer>
  <div class="abs brand" style="top:3136px;left:76px">
    <span class="name">QUILL</span>
    <span class="sub">REFRIGERATION</span>
  </div>
  <p class="abs footer-contact" style="top:3225px;left:75px;font-size:12px">Copyright © 2018 Quill Refrigeration<br>All Rights Reserved.</p>

  <div class="abs footer-head" style="top:3124px;left:373px">SITE MAP</div>
  <ul class="abs footer-list" style="top:3150px;left:373px"><li>Home</li><li>About</li><li>Services</li><li>Contact Us</li></ul>

  <div class="abs footer-head" style="top:3124px;left:617px">CONTACT US</div>
  <p class="abs footer-contact" style="top:3155px;left:617px">12 Harbour Lane<br>Joondalup WA 6027</p>
  <div class="abs footer-contact" style="top:3203px;left:617px;line-height:28px">
    <div style="display:flex;gap:22px;align-items:center"><svg width="12" height="12" viewBox="0 0 24 24"><path fill="#1c1c1c" d="M6.6 10.8a15 15 0 0 0 6.6 6.6l2.2-2.2a1 1 0 0 1 1-.25 11.4 11.4 0 0 0 3.6.6 1 1 0 0 1 1 1V20a1 1 0 0 1-1 1A17 17 0 0 1 3 4a1 1 0 0 1 1-1h3.5a1 1 0 0 1 1 1c0 1.25.2 2.45.6 3.6a1 1 0 0 1-.25 1z"/></svg>1-800-555-0147</div>
    <div style="display:flex;gap:22px;align-items:center"><svg width="12" height="12" viewBox="0 0 24 24"><rect x="2" y="5" width="20" height="14" fill="#1c1c1c"/><path d="M2 6l10 7 10-7" fill="none" stroke="#fff" stroke-width="1.6"/></svg>info@quillrefrigeration.example</div>
    <div style="display:flex;gap:22px;align-items:center"><svg width="12" height="12" viewBox="0 0 24 24"><path d="M12 2a7 7 0 0 0-7 7c0 5 7 13 7 13s7-8 7-13a7 7 0 0 0-7-7zm0 9.5A2.5 2.5 0 1 1 12 6.5a2.5 2.5 0 0 1 0 5z" fill="#1c1c1c"/></svg>Map Direction</div>
  </div>

  <div class="abs footer-head" style="top:3124px;left:907px">FOLLOW US</div>
  <div class="abs social" style="top:3163px;left:907px"><span></span><span></span><span></span><span></span></div>
</footer>

</body>
</html>
```